Business Cards and Stationery for CPA Firm
Gallowen & Company, P.C.
Business Cards and Stationery for CPA Firm -
Creative Brief
Professional
Bennett L. Gallowen
P.O. Box 482, 9 West Cedar Ave., Fernhollow, ST 00482
bgallowen@gallowencpa-example.com
www.gallowencpa-example.com
Need business cards and stationery for a CPA firm. I am open to design ideas and will provide feedback. Our generic email address for letterhead/fax is info@gallowencpa-example.com. This should be used in all locations except the business card. Each person with a business card will have his/her own email address.
Day - I've seen some with checkboxes for day of week. Other ideas welcome. Date Time Note

```html
<!DOCTYPE html>
<html lang="en">
<head>
<meta charset="utf-8">
<title>Gallowen &amp; Company, P.C. — Stationery Concepts</title>
<link href="https://fonts.googleapis.com/css2?family=Cinzel:wght@400;600&family=Open+Sans:wght@400;600&display=swap" rel="stylesheet">
<style>
:root{
  --bg-dark:#2f3032;
  --bg-light:#4a4b4e;
  --navy:#1f3552;
  --navy-deep:#15263d;
  --paper:#ffffff;
  --paper-shade:#eef0f3;
  --ink:#2a2f36;
  --muted:#8a9099;
  --rule:#c9ced6;
}
*{box-sizing:border-box;margin:0;padding:0}
html,body{width:1200px;height:310px;overflow:hidden}
body{
  position:relative;
  background:radial-gradient(ellipse at 30% 20%,var(--bg-light),var(--bg-dark) 70%);
  font-family:"Open Sans",Arial,sans-serif;color:var(--ink);
}
.piece{position:absolute}
.brand-name{font-family:"Cinzel",Georgia,serif;font-weight:600;letter-spacing:.3px;white-space:nowrap}
.brand-mark{display:inline-block;background:currentColor;vertical-align:middle}

/* presentation header */
.showcase-title{left:26px;top:26px;width:260px;color:var(--paper)}
.showcase-title .brand-mark{width:26px;height:26px}
.showcase-title .brand-name{font-size:14px;vertical-align:middle;margin-left:8px}
.showcase-title .tagline{font-size:5.5px;letter-spacing:1.8px;margin:2px 0 0 34px;border-top:1px solid var(--paper);padding-top:3px;width:190px;white-space:nowrap}
.concept-label{left:30px;top:92px;color:var(--paper);font-size:6px}

/* cards */
.card{width:112px;height:66px;padding:7px;font-size:4px;line-height:1.5;box-shadow:0 2px 5px rgba(0,0,0,.4);overflow:hidden}
.card.light{background:var(--paper);color:var(--ink)}
.card.dark{background:var(--navy);color:var(--paper)}
.card .brand-name{font-size:5.5px}
.card .brand-mark{width:8px;height:8px;margin-right:3px}
.card .role{color:var(--muted)}
.card .field{border-bottom:1px solid var(--rule);height:7px;margin-top:2px}
.card.dark .field{border-color:rgba(255,255,255,.4)}
.card h4{font-size:5px;font-weight:600}

/* letterhead */
.letterhead{width:140px;height:280px;background:var(--paper);padding:10px;font-size:3.6px;line-height:1.5;box-shadow:0 3px 8px rgba(0,0,0,.45)}
.letterhead .top{display:flex;justify-content:space-between;align-items:flex-start}
.letterhead .brand-name{font-size:5px;color:var(--navy)}
.letterhead .brand-mark{width:7px;height:7px;color:var(--navy);margin-right:2px}
.letterhead .contact{color:var(--muted);text-align:right;white-space:nowrap}
.letterhead .foot{position:absolute;bottom:8px;left:0;right:0;text-align:center;color:var(--muted);white-space:nowrap}
.letterhead.centered .top{justify-content:center}

/* notecards */
.notecard{width:140px;height:110px;background:var(--paper);font-size:3.6px;padding:8px;box-shadow:0 2px 6px rgba(0,0,0,.4);overflow:hidden}
.notecard .brand-name{font-size:5px;color:var(--navy)}
.notecard .brand-mark{width:7px;height:7px;color:var(--navy);margin-right:2px}
.notecard .band{position:absolute;left:0;right:0;bottom:0;height:14px;background:var(--navy);color:var(--paper);text-align:center;padding-top:4px}

/* envelopes */
.envelope{width:260px;height:88px;box-shadow:0 3px 8px rgba(0,0,0,.5);overflow:hidden}
.envelope.dark{background:var(--navy)}
.envelope.light{background:linear-gradient(var(--paper),var(--paper-shade))}
.envelope svg{position:absolute;inset:0}
.envelope .label{position:absolute;left:0;right:0;text-align:center;color:var(--paper);font-size:6px}
.envelope .label .brand-mark{width:8px;height:8px;margin-right:3px}
</style>
</head>
<body>

<header class="piece showcase-title">
  <span class="brand-mark"></span><span class="brand-name">GALLOWEN &amp; COMPANY, P.C.</span>
  <p class="tagline">CERTIFIED PUBLIC ACCOUNTANTS</p>
</header>
<p class="piece concept-label">Stationery Concepts</p>

<!-- business cards -->
<article class="piece card light" style="left:29px;top:110px">
  <span class="brand-mark" style="color:var(--navy)"></span><span class="brand-name" style="color:var(--navy)">Gallowen &amp; Company, P.C.</span>
  <p style="margin-top:10px;font-weight:600">Bennett L. Gallowen</p>
  <p class="role">Certified Public Accountant</p>
  <p style="margin-top:5px">bgallowen@gallowencpa-example.com</p>
</article>
<article class="piece card dark" style="left:149px;top:110px">
  <span class="brand-mark"></span><span class="brand-name">Gallowen &amp; Co.</span>
  <p style="margin-top:8px">P.O. Box 482, 9 West Cedar Ave.</p>
  <p>Fernhollow, ST 00482</p>
  <p>(555) 010-0142</p>
  <p>www.gallowencpa-example.com</p>
</article>

<!-- appointment cards -->
<article class="piece card light" style="left:29px;top:200px;height:88px">
  <h4>Appointment</h4>
  <div class="field">Day</div><div class="field">Date</div><div class="field">Time</div><div class="field">Note</div>
</article>
<article class="piece card dark" style="left:149px;top:200px;height:88px">
  <h4>Appointment</h4>
  <div class="field">Day</div><div class="field">Date</div><div class="field">Time</div><div class="field">Note</div>
</article>

<!-- letterheads -->
<article class="piece letterhead" style="left:340px;top:15px">
  <div class="top">
    <div><span class="brand-mark"></span><span class="brand-name">Gallowen &amp; Company, P.C.</span></div>
    <div class="contact">P.O. Box 482<br>Fernhollow, ST 00482<br>info@gallowencpa-example.com</div>
  </div>
  <p class="foot">www.gallowencpa-example.com</p>
</article>
<article class="piece letterhead centered" style="left:500px;top:15px">
  <div class="top">
    <div><span class="brand-mark"></span><span class="brand-name">Gallowen &amp; Company, P.C.</span></div>
  </div>
  <p class="foot">P.O. Box 482, Fernhollow, ST 00482 · info@gallowencpa-example.com</p>
</article>

<!-- notecards -->
<article class="piece notecard" style="left:690px;top:30px">
  <span class="brand-mark"></span><span class="brand-name">Gallowen &amp; Company, P.C.</span>
  <div class="band">www.gallowencpa-example.com</div>
</article>
<article class="piece notecard" style="left:690px;top:170px">
  <span class="brand-mark"></span><span class="brand-name">Gallowen &amp; Company, P.C.</span>
  <div class="band">info@gallowencpa-example.com</div>
</article>

<!-- envelopes -->
<article class="piece envelope dark" style="left:912px;top:14px">
  <svg width="260" height="88" aria-hidden="true"><polygon points="0,0 130,40 260,0" fill="var(--navy-deep)"/></svg>
  <div class="label" style="top:50px"><span class="brand-mark"></span><span class="brand-name">Gallowen &amp; Company</span></div>
</article>
<article class="piece envelope light" style="left:912px;top:111px">
  <svg width="260" height="88" aria-hidden="true"><polygon points="0,0 130,40 260,0" fill="none" stroke="var(--rule)"/></svg>
</article>
<article class="piece envelope light" style="left:912px;top:208px">
  <svg width="260" height="88" aria-hidden="true"><polygon points="0,0 130,34 260,0" fill="var(--paper-shade)" stroke="var(--rule)"/></svg>
  <div class="label" style="color:var(--navy);top:56px"><span class="brand-mark"></span><span class="brand-name">Gallowen &amp; Company</span></div>
</article>

</body>
</html>
```